Home Renovation Business needs a logo and business card design

I need a logo design for my home renovation company. I work hard to provide quality work for a fair price. I want a clean design that has something to make it pop and catch the eye. It should have somewhat of a modern feel to it. You can check out my website at www.kolbrenhomes.com to see some examples of the type of work I do.
Updates

Hi Everyone,

For some reason, not all my information was posted. I would like the following contact information included in the design:

Phone: 365.412.7958        Email: tkeswick@orvale.ca        Website: www.kolbrenhomes.com

Also, if you would like to include a list of the services I offer, then I'd like the card to be double sided. I provide the following services: Full kitchen, basement and bathroom renovations. Tile, laminate and hardwood installation. Decks, fences and sheds. Windows and doors.

Industry/Entity Type

Business

Requirements
Must have
• I want the following information listed on the card:
• TK Renovations
• Tom Keswickle
• 365.412.7958
• tkeswick@orvale.ca
• www.kolbrenhomes.com
Nice to have
• If you want you could also include the list of services I provide. If you include this list feel free to make the card double sided.
• Kitchen, bathroom and basement renovations
• Flooring installation
• Decks, fences and sheds
• Windows and doors
• I am not 100% sure if I want to include this on the card or not.

```html
<!DOCTYPE html>
<html lang="en">
<head>
<meta charset="utf-8">
<title>TK Renovations – Business Card</title>
<link href="https://fonts.googleapis.com/css2?family=Anton&family=Arimo:wght@400&display=swap" rel="stylesheet">
<style>
  :root {
    --canvas: #ffffff;
    --card-blue: #3fa2da;
    --dark-1: #2b2b2d;
    --dark-2: #4a4a4c;
    --stripe: #6e7378;
    --text-light: #ffffff;
    --text-dark: #1f1f1f;
  }
  * { margin: 0; padding: 0; box-sizing: border-box; }
  html, body {
    width: 1200px; height: 353px; overflow: hidden;
    background: var(--canvas);
  }
  .sheet { position: relative; width: 1200px; height: 353px; }
  .card {
    position: absolute; top: 0; width: 585px; height: 353px;
    background: var(--card-blue); overflow: hidden;
  }
  .card--front { left: 0; }
  .card--back { left: 615px; }
  .card__backdrop { position: absolute; inset: 0; width: 100%; height: 100%; }

  .brand-name {
    position: absolute; color: var(--text-light);
    font-family: "Anton", "Arial Narrow", sans-serif;
    font-weight: 400; letter-spacing: 0.5px; line-height: 1; white-space: nowrap;
  }
  .website {
    position: absolute; color: var(--text-light);
    font-family: "Arimo", Arial, sans-serif; line-height: 1; white-space: nowrap;
  }
  .card--front .brand-name { left: 128px; top: 26px; font-size: 52px; }
  .card--front .website { left: 246px; top: 86px; font-size: 24px; }

  .contact {
    position: absolute; left: 12px; top: 268px; list-style: none;
    color: var(--text-light); font-family: "Arimo", Arial, sans-serif;
    font-size: 16px; line-height: 22px;
  }

  .services {
    position: absolute; left: 0; top: 28px; list-style: none;
    font-family: "Arimo", Arial, sans-serif; font-size: 18px; color: var(--text-dark);
  }
  .services__item { position: absolute; white-space: nowrap; line-height: 1; }
  .services__item::before {
    content: ""; display: inline-block; width: 6px; height: 6px; border-radius: 50%;
    background: var(--text-dark); margin-right: 8px; vertical-align: middle;
    position: relative; top: -2px;
  }
  .services__item:nth-child(1) { left: 48px;  top: 0; }
  .services__item:nth-child(2) { left: 90px;  top: 40px; }
  .services__item:nth-child(3) { left: 128px; top: 76px; }
  .services__item:nth-child(4) { left: 162px; top: 110px; }

  .card--back .brand-name { left: 196px; top: 278px; font-size: 34px; }
  .card--back .website { left: 216px; top: 322px; font-size: 17px; }
</style>
</head>
<body>
<main class="sheet">
  <section class="card card--front">
    <svg class="card__backdrop" viewBox="0 0 585 353" preserveAspectRatio="none" aria-hidden="true">
      <defs>
        <linearGradient id="front-dark" x1="0" y1="0" x2="1" y2="1">
          <stop offset="0" stop-color="var(--dark-2)"/>
          <stop offset="0.6" stop-color="var(--dark-1)"/>
          <stop offset="1" stop-color="#39393b"/>
        </linearGradient>
      </defs>
      <polygon points="0,0 120,0 400,353 0,353" fill="url(#front-dark)"/>
      <polygon points="120,0 148,0 428,353 400,353" fill="var(--stripe)"/>
    </svg>
    <div class="brand-name">TK Renovations</div>
    <div class="website">www.kolbrenhomes.com</div>
    <ul class="contact">
      <li>phone: 365.412.7958</li>
      <li>email: tkeswick@orvale.ca</li>
    </ul>
  </section>

  <section class="card card--back">
    <svg class="card__backdrop" viewBox="0 0 590 353" preserveAspectRatio="none" aria-hidden="true">
      <defs>
        <linearGradient id="back-dark" x1="0" y1="0" x2="1" y2="1">
          <stop offset="0" stop-color="var(--dark-2)"/>
          <stop offset="0.6" stop-color="var(--dark-1)"/>
          <stop offset="1" stop-color="#39393b"/>
        </linearGradient>
      </defs>
      <polygon points="0,20 0,353 440,353 100,0 20,0" fill="url(#back-dark)"/>
      <polygon points="100,0 128,0 468,353 440,353" fill="var(--stripe)"/>
    </svg>
    <ul class="services">
      <li class="services__item">full kitchen, basement and bathroom renovations</li>
      <li class="services__item">tile, laminate and hardwood installation</li>
      <li class="services__item">decks, fences and sheds</li>
      <li class="services__item">windows and doors</li>
    </ul>
    <div class="brand-name">TK Renovations</div>
    <div class="website">www.kolbrenhomes.com</div>
  </section>
</main>
</body>
</html>
```